Auto Mechanic business card

Need a general business card for GearFixer.
Name on card should be 'Roadside Wrench'
Tel # (869) 412 3097
Address is - Palm Lane, Basseterre, St. Kitts
Whatsapp and facebook symbols should be added
On back of card should include services offered
General Repairs
Brakes
Tune Ups
Suspensions
Oil Leaks
Dent repairs
Suspensions
Car Sales
Tyre Repairs
General service
Check Engine Light
Minor Electricals

Target Market(s)

General Population, University students

Industry/Entity Type

Auto Mechanic

Contact Information for Business Card

Roadside Wrench

Requirements
Must have
• 2 Sides

```html
<!DOCTYPE html>
<html lang="en">
<head>
<meta charset="utf-8">
<title>Roadside Wrench – Business Card</title>
<link rel="stylesheet" href="https://fonts.googleapis.com/css2?family=Montserrat:wght@600&family=Arimo:wght@400&family=Michroma&display=swap">
<style>
  :root {
    --stage: #3a3a3a;
    --red: #d62527;
    --white: #ffffff;
    --charcoal: #3b3b3d;
    --ink: #2f2f31;
    --social-a: #3d5a98;
    --social-b: #25a33a;
  }
  * { box-sizing: border-box; margin: 0; padding: 0; }
  html, body {
    width: 1200px; height: 1015px; overflow: hidden;
    background: var(--stage);
  }
  .stage {
    position: relative; width: 1200px; height: 1015px;
  }
  .card {
    position: absolute; left: 220px; width: 760px; height: 434px;
    overflow: hidden; box-shadow: 0 10px 30px rgba(0,0,0,.45);
  }

  /* Services side */
  .card--services { top: 52px; background: var(--red); color: var(--white); }
  .brand {
    position: absolute; display: flex; align-items: center; gap: 14px;
    font-family: "Montserrat", sans-serif; font-weight: 600; white-space: nowrap;
  }
  .brand__mark { width: 34px; height: 34px; border: 4px solid currentColor; border-radius: 4px; }
  .card--services .brand { left: 50%; top: 96px; transform: translateX(-50%); font-size: 44px; }
  .services {
    position: absolute; top: 272px; left: 70px; right: 50px;
    display: flex; justify-content: space-between;
    font-family: "Arimo", sans-serif; font-size: 19px; line-height: 1.32;
    list-style: none;
  }
  .services ul { list-style: none; }
  .services li::before {
    content: ""; display: inline-block; width: 9px; height: 9px;
    border-radius: 50%; background: var(--white); margin-right: 8px; vertical-align: 2px;
  }
  .services ul:nth-child(1) { margin-top: 60px; }
  .services ul:nth-child(3) { margin-top: -30px; }

  /* Contact side */
  .card--contact { top: 530px; background: var(--white); }
  .card--contact .brand { left: 50%; top: 118px; transform: translateX(-50%); font-size: 48px; color: var(--ink); }
  .card--contact .brand__mark { border-color: var(--red); }
  .info-band {
    position: absolute; left: 0; right: 0; top: 272px; height: 52px;
    background: var(--charcoal); color: var(--white);
    display: flex; align-items: center; justify-content: space-between; padding: 0 30px 0 40px;
    font-family: "Arimo", sans-serif; font-size: 19px;
  }
  .address { display: flex; align-items: center; gap: 10px; }
  .social { display: flex; gap: 8px; }
  .social span { width: 28px; height: 28px; border-radius: 50%; display: block; }
  .social .social--a { background: var(--social-a); }
  .social .social--b { background: var(--social-b); }
  .phone-band {
    position: absolute; left: 0; right: 0; top: 332px; bottom: 0;
    background: var(--red); color: var(--white);
    display: flex; align-items: center; justify-content: center;
    font-family: "Michroma", sans-serif; font-size: 40px; letter-spacing: 2px;
  }
</style>
</head>
<body>
<main class="stage">
  <section class="card card--services" aria-label="Services side">
    <div class="brand"><span class="brand__mark"></span>Roadside Wrench</div>
    <div class="services">
      <ul>
        <li>General Repairs</li>
        <li>Brakes</li>
        <li>Tune Ups</li>
        <li>Suspensions</li>
      </ul>
      <ul>
        <li>Suspensions</li>
        <li>Car Sales</li>
        <li>Tyre Repairs</li>
        <li>General service</li>
      </ul>
      <ul>
        <li>Check Engine Light</li>
        <li>Minor Electricals</li>
        <li>Oil Leaks</li>
        <li>Dent repairs</li>
      </ul>
    </div>
  </section>

  <section class="card card--contact" aria-label="Contact side">
    <div class="brand"><span class="brand__mark"></span>Roadside Wrench</div>
    <div class="info-band">
      <div class="address">
        <svg width="18" height="24" viewBox="0 0 18 24" aria-hidden="true">
          <path d="M9 0C4 0 0 4 0 9c0 6.5 9 15 9 15s9-8.5 9-15c0-5-4-9-9-9z" fill="#d62527"/>
          <circle cx="9" cy="9" r="3.5" fill="#3b3b3d"/>
        </svg>
        <span>Palm Lane, Basseterre, St. Kitts</span>
      </div>
      <div class="social" role="img" aria-label="Social profiles">
        <span class="social--a"></span>
        <span class="social--b"></span>
      </div>
    </div>
    <div class="phone-band"># (869) 412 3097</div>
  </section>
</main>
</body>
</html>
```